Quimby's Yard & Garden Center Business Card Update

I need an updated Business card design for my Lawn and Garden Center. We do Landscaping installs, Lawn Mowing, Snow Removal and also have a Garden Center Retail Division. I uploaded a few of our previous business cards to give an idea of what we are starting with. The main goal of this update is to simplify and modernize the business card, not all of the services that are on the previous cards has to be on the new one but I would still like to highlight our main services. There is also a sample of our logo that Can be used in the design.

Industry/Entity Type

Landscaping

Contact Information for Business Card

Morris Quimby
Morris@Quimbysyardandgarden.example
Business (555) 201-7784
Cell (555) 318-6092

Colors

Designer to choose colors to be used in the design.

Requirements
Must have
• Services Provided :
• Landscaping
• Lawn Maintenance
• Snow Removal
• Garden Center

```html
<!DOCTYPE html>
<html lang="en">
<head>
<meta charset="utf-8">
<title>Quimby's Yard &amp; Garden Center – Business Card</title>
<link rel="stylesheet" href="https://fonts.googleapis.com/css2?family=Open+Sans:wght@400;600;700&family=Kaushan+Script&display=swap">
<style>
  :root {
    --green: #2c4f25;
    --green-mark: #2f5a27;
    --paper: #f1f1f1;
    --white: #ffffff;
    --orange: #eaa43a;
    --backdrop: #d9d9d9;
  }
  * { box-sizing: border-box; margin: 0; padding: 0; }
  html, body { width: 1200px; height: 1021px; overflow: hidden; }
  body {
    background: var(--backdrop);
    font-family: "Open Sans", sans-serif;
    display: flex;
    flex-direction: column;
    align-items: center;
    justify-content: center;
    gap: 34px;
  }
  .card {
    position: relative;
    width: 820px;
    height: 469px;
    overflow: hidden;
    box-shadow: 0 6px 18px rgba(0,0,0,.25);
  }
  /* Front */
  .card-front { background: var(--green); color: var(--white); }
  .tagline {
    position: absolute; left: 70px; top: 78px;
    font-family: "Kaushan Script", cursive;
    color: var(--orange); font-size: 30px;
  }
  .services { position: absolute; left: 76px; top: 140px; list-style: none; }
  .services li {
    display: flex; align-items: center; gap: 14px;
    font-size: 19px; font-weight: 600; letter-spacing: .5px;
    text-transform: uppercase; line-height: 36px;
  }
  .services li::before {
    content: ""; width: 10px; height: 10px; border-radius: 50%;
    background: var(--white);
  }
  .wordmark {
    position: absolute; display: flex; align-items: center; justify-content: center;
    gap: 14px; font-family: "Open Sans", sans-serif; font-weight: 700;
    white-space: nowrap;
  }
  .wordmark .dot { width: 24px; height: 24px; border-radius: 50%; flex: none; }
  .card-front .wordmark { right: 70px; top: 250px; color: var(--white); font-size: 60px; }
  .card-front .wordmark .dot { background: var(--white); }
  /* Back */
  .card-back { background: var(--paper); }
  .card-back .split { position: absolute; inset: 0; }
  .contact {
    position: absolute; left: 60px; top: 70px; color: var(--white);
  }
  .contact .name { font-size: 26px; font-weight: 700; text-transform: uppercase; letter-spacing: .5px; }
  .contact .role { font-size: 17px; text-transform: uppercase; margin-bottom: 40px; }
  .contact .address { font-size: 19px; line-height: 26px; margin-bottom: 6px; }
  .contact ul { list-style: none; }
  .contact li { display: flex; align-items: center; gap: 10px; font-size: 19px; line-height: 28px; }
  .contact svg { width: 16px; height: 16px; flex: none; }
  .card-back .wordmark {
    left: 515px; right: 24px; top: 150px;
    color: var(--green-mark); font-size: 48px;
  }
  .card-back .wordmark .dot { background: var(--green-mark); width: 20px; height: 20px; }
</style>
</head>
<body>
  <section class="card card-front" aria-label="Card front">
    <p class="tagline">Where Color Lives...</p>
    <ul class="services">
      <li>Landscaping</li>
      <li>Lawn Maintenance</li>
      <li>Snow Removal</li>
      <li>Garden Center</li>
    </ul>
    <div class="wordmark"><span class="dot"></span>Quimby's</div>
  </section>

  <section class="card card-back" aria-label="Card back">
    <svg class="split" viewBox="0 0 820 469" preserveAspectRatio="none">
      <polygon points="0,0 470,0 520,469 0,469" fill="var(--green)"/>
    </svg>
    <div class="contact">
      <p class="name">Morris Quimby</p>
      <p class="role">Co-Owner</p>
      <p class="address">4820 Orchard Lane<br>Maple Falls, OHIO 45000</p>
      <ul>
        <li><svg viewBox="0 0 16 16"><path d="M3 1l3 3-2 2c1 2 3 4 6 6l2-2 3 3-2 2C7 15 1 9 1 3z" fill="#fff"/></svg>(555) 201-7784</li>
        <li><svg viewBox="0 0 16 16"><rect x="4" y="1" width="8" height="14" rx="1.5" fill="none" stroke="#fff" stroke-width="1.5"/></svg>(555) 318-6092</li>
        <li><svg viewBox="0 0 16 16"><rect x="1" y="3" width="14" height="10" fill="none" stroke="#fff" stroke-width="1.5"/><path d="M1 3l7 6 7-6" fill="none" stroke="#fff" stroke-width="1.5"/></svg>Morris@Quimbysyardandgarden.example</li>
        <li><svg viewBox="0 0 16 16"><circle cx="8" cy="8" r="6.5" fill="none" stroke="#fff" stroke-width="1.5"/><path d="M1.5 8h13M8 1.5c-3 3.5-3 9.5 0 13M8 1.5c3 3.5 3 9.5 0 13" fill="none" stroke="#fff" stroke-width="1.2"/></svg>www.Quimbysyardandgarden.example</li>
      </ul>
    </div>
    <div class="wordmark"><span class="dot"></span>Quimby's</div>
  </section>
</body>
</html>
```